Corporate PowerPoint Template

Seeking a Powerpoint Template Design for High Technology company based in Silicon Valley. We are seeking a general template design that conveys a professional, clean, progressive message.

The Template must have the following elements at a minimum:
1. Title Page (see comments following)
2. Agenda Page
3. Page Number, Date and Confidentiality Statement
Items in #3 are to appear on all pages except title page

We expect the Title page to be graphical in nature with area for Presentation Title, Presenter Name, Date and a place for confidentiality statement should be present as well. Three (3) distinct Title pages to address different constituencies: Customers, Partners and Internal Communications.

In general, we would like to stay with our corporate color scheme (which may be found in our logo). To better understand our products, logo and look and feel - please visit our website at: http://www.varmelith.example

```html
<!DOCTYPE html>
<html lang="en">
<head>
<meta charset="utf-8">
<title>Varmelith Presentation Template</title>
<link href="https://fonts.googleapis.com/css2?family=Quicksand:wght@500;600&family=Didact+Gothic&display=swap" rel="stylesheet">
<style>
  :root {
    --backdrop-top: #ddeff8;
    --backdrop-bottom: #e8f5fb;
    --teal-deep: #054b55;
    --teal-dark: #06606a;
    --teal: #0d7f84;
    --teal-panel: #047a8b;
    --series-1: #0e8180;
    --series-2: #6a93cf;
    --series-3: #07636a;
    --grey-text: #8c8c8c;
    --axis: #b5b5b5;
    --label: #333333;
    --white: #ffffff;
  }
  * { margin: 0; padding: 0; box-sizing: border-box; }
  html, body { width: 900px; height: 1200px; overflow: hidden; }
  body {
    position: relative;
    background: linear-gradient(180deg, var(--backdrop-top), var(--backdrop-bottom));
    font-family: "Didact Gothic", "Century Gothic", sans-serif;
  }
  .slide {
    position: absolute;
    left: 103px;
    width: 694px;
    height: 520px;
    background: var(--white);
    box-shadow: 0 2px 6px rgba(0, 0, 0, 0.25);
    overflow: hidden;
  }
  .slide--title { top: 67px; }
  .slide--charts { top: 613px; background: linear-gradient(160deg, #ffffff 50%, #eef1f8); }

  .title-band {
    position: absolute; left: 0; top: 0; width: 694px; height: 106px;
    background: linear-gradient(180deg, var(--teal-deep), #075a64);
  }
  .photo { position: absolute; }
  .photo--cubes { left: 0; top: 106px; width: 320px; height: 282px;
    background: radial-gradient(circle at 45% 55%, #d9d9d9, #9a9a9a 70%, #7d7d7d); }
  .photo--keys { left: 502px; top: 106px; width: 192px; height: 97px;
    background: linear-gradient(160deg, #8a8a8a, #4a4a4a); }
  .photo--chip { left: 502px; top: 203px; width: 192px; height: 185px;
    background: linear-gradient(170deg, #b7b7b7, #8e8e8e 60%, #a5a5a5); }
  .audience-panel {
    position: absolute; left: 320px; top: 106px; width: 182px; height: 282px;
    background: var(--teal-panel);
    box-shadow: 3px 0 6px rgba(0, 0, 0, 0.3);
  }
  .audience-panel__label {
    position: absolute; left: 17px; top: 132px;
    font-family: "Quicksand", sans-serif; font-weight: 500;
    font-size: 16px; color: var(--white); letter-spacing: 0.2px;
  }
  .title-foot { position: absolute; left: 0; top: 388px; width: 694px; height: 132px; }
  .brand-name {
    position: absolute;
    font-family: "Quicksand", sans-serif; font-weight: 600;
    color: var(--teal-dark);
  }
  .brand-dot { position: absolute; border-radius: 50%; background: var(--teal); }
  .title-foot .brand-dot { left: 38px; top: 40px; width: 48px; height: 48px; }
  .title-foot .brand-name { left: 104px; top: 38px; font-size: 38px; }

  .meta { position: absolute; font-size: 11px; color: var(--grey-text); }
  .meta--presenter { left: 244px; }
  .meta--date { left: 527px; }
  .meta--page { left: 647px; font-size: 8px; }
  .title-foot .meta { top: 99px; }
  .title-foot .meta--page { top: 101px; }

  .charts-header {
    position: absolute; left: 0; top: 0; width: 694px; height: 92px;
    background: linear-gradient(90deg, #07555f, var(--teal) 60%, #138a8c);
    border-bottom: 1px solid #0a4c54;
  }
  .charts-header__title {
    position: absolute; left: 42px; top: 34px;
    font-family: "Quicksand", sans-serif; font-weight: 600;
    font-size: 27px; color: var(--white);
  }
  .charts-header__confidential {
    position: absolute; right: 13px; top: 12px; font-size: 11px; color: var(--white);
  }
  .chart-heading {
    position: absolute; top: 117px; width: 307px; height: 47px;
    background: linear-gradient(180deg, #e4eeef, #a9c7c9);
    font-family: "Quicksand", sans-serif; font-weight: 600;
    font-size: 17px; color: var(--teal);
    display: flex; align-items: center; justify-content: center;
  }
  .chart-heading--one { left: 34px; }
  .chart-heading--two { left: 353px; }
  .chart-art { position: absolute; left: 0; top: 0; width: 694px; height: 520px; }
  .chart-art text { font-family: "Didact Gothic", sans-serif; fill: var(--label); }
  .tick { font-size: 13px; }
  .cat { font-size: 14px; }
  .legend { font-size: 13px; }

  .charts-foot .brand-dot { left: 15px; top: 484px; width: 24px; height: 24px; }
  .charts-foot .brand-name { left: 48px; top: 483px; font-size: 20px; }
  .charts-foot .meta { top: 488px; }
  .charts-foot .meta--page { top: 489px; }
</style>
</head>
<body>

<section class="slide slide--title">
  <div class="title-band"></div>
  <div class="photo photo--cubes" role="img" aria-label="Photograph of stacked silver and glass cubes"></div>
  <div class="audience-panel"><span class="audience-panel__label">CUSTOMERS</span></div>
  <div class="photo photo--keys" role="img" aria-label="Close-up photograph of a keyboard"></div>
  <div class="photo photo--chip" role="img" aria-label="Close-up photograph of a connector chip on a circuit board"></div>
  <div class="title-foot">
    <span class="brand-dot"></span>
    <span class="brand-name">varmelith</span>
    <span class="meta meta--presenter">Presenter Name</span>
    <span class="meta meta--date">30 August 2014</span>
    <span class="meta meta--page">3</span>
  </div>
</section>

<section class="slide slide--charts">
  <header class="charts-header">
    <h1 class="charts-header__title">Sample Slide Charts 2</h1>
    <span class="charts-header__confidential">Strictly Confidential</span>
  </header>
  <div class="chart-heading chart-heading--one">Chart 1</div>
  <div class="chart-heading chart-heading--two">Chart 2</div>

  <svg class="chart-art" viewBox="103 613 694 520" xmlns="http://www.w3.org/2000/svg">
    <!-- Chart 1: clustered columns -->
    <g class="chart chart--clustered">
      <line x1="163" y1="790" x2="163" y2="1002" stroke="var(--axis)"/>
      <line x1="163" y1="1002" x2="432" y2="1002" stroke="var(--axis)"/>
      <g class="tick" text-anchor="end">
        <text x="153" y="1007">0</text><text x="153" y="972">1</text>
        <text x="153" y="937">2</text><text x="153" y="901">3</text>
        <text x="153" y="866">4</text><text x="153" y="830">5</text>
        <text x="153" y="795">6</text>
      </g>
      <g fill="var(--series-1)">
        <rect x="175" y="850.2" width="15" height="151.8"/>
        <rect x="242" y="913.7" width="15" height="88.3"/>
        <rect x="310" y="878.4" width="15" height="123.6"/>
        <rect x="377" y="843.1" width="15" height="158.9"/>
      </g>
      <g fill="var(--series-2)">
        <rect x="190" y="917.3" width="15" height="84.7"/>
        <rect x="257" y="846.7" width="15" height="155.3"/>
        <rect x="325" y="938.5" width="15" height="63.5"/>
        <rect x="392" y="903.2" width="15" height="98.8"/>
      </g>
      <g fill="var(--series-3)">
        <rect x="205" y="931.4" width="15" height="70.6"/>
        <rect x="272" y="931.4" width="15" height="70.6"/>
        <rect x="340" y="896.1" width="15" height="105.9"/>
        <rect x="407" y="825.5" width="15" height="176.5"/>
      </g>
      <g class="cat" text-anchor="middle">
        <text x="198" y="1025">Category</text><text x="198" y="1041">1</text>
        <text x="265" y="1025">Category</text><text x="265" y="1041">2</text>
        <text x="333" y="1025">Category</text><text x="333" y="1041">3</text>
        <text x="400" y="1025">Category</text><text x="400" y="1041">4</text>
      </g>
      <g class="legend">
        <rect x="194" y="1056" width="7" height="7" fill="var(--series-1)"/><text x="203" y="1065">Series 1</text>
        <rect x="265" y="1056" width="7" height="7" fill="var(--series-2)"/><text x="274" y="1065">Series 2</text>
        <rect x="336" y="1056" width="7" height="7" fill="var(--series-3)"/><text x="345" y="1065">Series 3</text>
      </g>
    </g>

    <!-- Chart 2: stacked columns -->
    <g class="chart chart--stacked">
      <line x1="488" y1="791" x2="488" y2="1002" stroke="var(--axis)"/>
      <line x1="488" y1="1002" x2="752" y2="1002" stroke="var(--axis)"/>
      <g class="tick" text-anchor="end">
        <text x="478" y="1007">0</text><text x="478" y="977">2</text>
        <text x="478" y="947">4</text><text x="478" y="916">6</text>
        <text x="478" y="886">8</text><text x="478" y="856">10</text>
        <text x="478" y="826">12</text><text x="478" y="796">14</text>
      </g>
      <g fill="var(--series-1)">
        <rect x="509" y="937.2" width="27" height="64.8"/>
        <rect x="575" y="964.3" width="27" height="37.7"/>
        <rect x="640" y="949.3" width="27" height="52.7"/>
        <rect x="706" y="934.2" width="27" height="67.8"/>
      </g>
      <g fill="var(--series-2)">
        <rect x="509" y="901.0" width="27" height="36.2"/>
        <rect x="575" y="898.0" width="27" height="66.3"/>
        <rect x="640" y="922.2" width="27" height="27.1"/>
        <rect x="706" y="892.0" width="27" height="42.2"/>
      </g>
      <g fill="var(--series-3)">
        <rect x="509" y="870.9" width="27" height="30.1"/>
        <rect x="575" y="867.9" width="27" height="30.1"/>
        <rect x="640" y="877.0" width="27" height="45.2"/>
        <rect x="706" y="816.6" width="27" height="75.4"/>
      </g>
      <g class="cat" text-anchor="middle">
        <text x="522" y="1025">Category</text><text x="522" y="1041">1</text>
        <text x="588" y="1025">Category</text><text x="588" y="1041">2</text>
        <text x="654" y="1025">Category</text><text x="654" y="1041">3</text>
        <text x="720" y="1025">Category</text><text x="720" y="1041">4</text>
      </g>
      <g class="legend">
        <rect x="512" y="1056" width="7" height="7" fill="var(--series-1)"/><text x="521" y="1065">Series 1</text>
        <rect x="583" y="1056" width="7" height="7" fill="var(--series-2)"/><text x="592" y="1065">Series 2</text>
        <rect x="654" y="1056" width="7" height="7" fill="var(--series-3)"/><text x="663" y="1065">Series 3</text>
      </g>
    </g>
  </svg>

  <footer class="charts-foot">
    <span class="brand-dot"></span>
    <span class="brand-name">varmelith</span>
    <span class="meta meta--presenter">Presenter Name</span>
    <span class="meta meta--date">30 August 2014</span>
    <span class="meta meta--page">9</span>
  </footer>
</section>

</body>
</html>
```